IT Company based on Biology Business Needs a Business Card Design

We need a business card design for a new company called 'Lumen CELL'. We develop the machine learning solutions especially focused on deep learning algorithms for biology industry. Our initial product is a vision detection on biological images to help doctors diagnose the symptoms. We would like to see designs that use the color green.

Industry/Entity Type

Business

```html
<!DOCTYPE html>
<html lang="en">
<head>
<meta charset="utf-8">
<title>Lumen CELL business card</title>
<link rel="stylesheet" href="https://fonts.googleapis.com/css2?family=Montserrat:wght@500;600&family=Source+Sans+3:wght@400&display=swap">
<style>
  :root {
    --backdrop: #e7e7e7;
    --card: #fbfbfb;
    --brand-green: #4bb33a;
    --deep-green: #157a38;
    --text-green: #2f9a3a;
    --divider: #e3e3e3;
  }
  * { box-sizing: border-box; margin: 0; padding: 0; }
  html, body {
    width: 1200px; height: 1200px; overflow: hidden;
    background: var(--backdrop);
  }
  .canvas {
    position: relative; width: 1200px; height: 1200px;
  }
  .card {
    position: absolute; left: 230px; width: 740px; height: 420px;
    background: var(--card);
    box-shadow: 0 6px 18px rgba(0,0,0,0.12);
  }
  .card--front { top: 150px; }
  .card--back { top: 630px; }

  .brand {
    display: flex; align-items: center; gap: 16px;
    font-family: "Montserrat", sans-serif; font-weight: 500;
    color: var(--brand-green); letter-spacing: -1px;
    white-space: nowrap;
  }
  .brand__dot {
    width: 28px; height: 28px; border-radius: 50%;
    background: var(--brand-green); flex: none;
  }
  .card--front .brand {
    position: absolute; left: 0; right: 0; top: 0; bottom: 0;
    justify-content: center; font-size: 60px;
  }
  .card--back .brand-area {
    position: absolute; left: 0; top: 0; bottom: 0; width: 370px;
    display: flex; align-items: center; justify-content: center;
  }
  .card--back .brand { font-size: 38px; gap: 12px; }
  .card--back .brand__dot { width: 18px; height: 18px; }

  .card__divider {
    position: absolute; left: 370px; top: 30px; bottom: 30px;
    width: 1px; background: var(--divider);
  }
  .contact {
    position: absolute; left: 405px; top: 60px; right: 30px;
    font-family: "Source Sans 3", sans-serif; color: var(--text-green);
    font-size: 19px; line-height: 1.3;
  }
  .contact__name {
    font-family: "Montserrat", sans-serif; font-weight: 600;
    font-size: 28px; color: var(--deep-green);
  }
  .contact__title { font-size: 16px; margin-bottom: 26px; }
  .contact__list { list-style: none; margin-bottom: 14px; }
  .contact__item { display: flex; align-items: center; gap: 14px; }
  .contact__icon { width: 16px; height: 16px; flex: none; }
  .contact__address { font-size: 19px; }
</style>
</head>
<body>
<main class="canvas">
  <section class="card card--front">
    <div class="brand"><span class="brand__dot"></span><span class="brand__name">Lumen CELL</span></div>
  </section>

  <section class="card card--back">
    <div class="brand-area">
      <div class="brand"><span class="brand__dot"></span><span class="brand__name">Lumen CELL</span></div>
    </div>
    <div class="card__divider"></div>
    <div class="contact">
      <h1 class="contact__name">Your name</h1>
      <p class="contact__title">Your Title</p>
      <ul class="contact__list">
        <li class="contact__item">
          <svg class="contact__icon" viewBox="0 0 16 16"><path fill="currentColor" d="M2 6c0-2 2.5-3 6-3s6 1 6 3v1h-3V5.5c-1.8-.6-4.2-.6-6 0V7H2zM4 8h8l2 6H2z"/></svg>
          <span>+00 111 222 3333</span>
        </li>
        <li class="contact__item">
          <svg class="contact__icon" viewBox="0 0 16 16"><rect x="1" y="3" width="14" height="10" fill="currentColor"/><path d="M1 3l7 6 7-6" fill="none" stroke="#fbfbfb" stroke-width="1.4"/></svg>
          <span>yourname@yourwebsite.com</span>
        </li>
        <li class="contact__item">
          <svg class="contact__icon" viewBox="0 0 16 16"><circle cx="8" cy="8" r="6.5" fill="currentColor"/><path d="M1.5 8h13M8 1.5v13M3 4.5h10M3 11.5h10" stroke="#fbfbfb" stroke-width="0.9" fill="none"/></svg>
          <span>www.yourwebsite.com</span>
        </li>
      </ul>
      <p class="contact__address">Your Long Commercial or<br>business address in 2 line</p>
    </div>
  </section>
</main>
</body>
</html>
```